Orin Care- Welcome

Under New Management / New Staff & New Physicians

Offering More Services

Accepting New Patients

Two Locations in the Bronx: North Bronx: 5912 Larkfield Blvd – Office Phone: 718-555-0143
South Bronx: 614 Dorrin Avenue – Office Phone: 718-555-0187

Our Services:
Primary Care
Gynecology
Cardiology
Dentistry
Psychology
Psychiatry
Neurology
Pain Management
Gastroenterology
Podiatry
Dermatology
Vascular Surgery
Physical Therapy
HIV / Infectious Disease

For an QPRL Mailing - we will drop off to Post Office

Front English
Back Smaller to have post office specs but have it in Spanish

```html
<!DOCTYPE html>
<html lang="en">
<head>
<meta charset="utf-8">
<title>Orin Care – Welcome Mailer</title>
<link rel="stylesheet" href="https://fonts.googleapis.com/css2?family=Oswald:wght@500;600;700&family=Montserrat:wght@500;700;800&family=Nunito:wght@600;700&family=Arimo&display=swap">
<style>
:root{
  --navy:#0d2a6e;
  --red:#b0000f;
  --ink:#1c1c1c;
  --paper:#ffffff;
  --paper-shade:#eeeff2;
  --stage:#5b5b5b;
  --photo-a:#8fb0e0;
  --photo-b:#d9c2b0;
}
*{margin:0;padding:0;box-sizing:border-box}
html,body{width:812px;height:1200px;overflow:hidden}
body{background:var(--stage);position:relative;font-family:'Nunito',sans-serif}
.card{position:absolute;overflow:hidden;background:var(--paper)}
.card > svg.bg{position:absolute;left:0;top:0}
.abs{position:absolute}

/* front */
.front{left:70px;top:71px;width:672px;height:480px;background:linear-gradient(100deg,var(--paper-shade),var(--paper) 55%)}
.headline{left:32px;top:26px;font-family:'Oswald',sans-serif;font-weight:700;font-size:25px;line-height:30px;color:var(--navy);text-transform:uppercase}
.headline .hot{color:var(--red)}
.offering{left:32px;top:98px;font-family:'Montserrat',sans-serif;font-weight:800;font-size:31px;line-height:33px;color:#fff}
.accepting{left:34px;top:176px;font-family:'Montserrat',sans-serif;font-weight:800;font-size:45px;line-height:48px;color:var(--red);letter-spacing:-.5px}
.new-patients{left:34px;top:222px;width:259px;height:36px;background:var(--navy);color:#fff;font-family:'Montserrat',sans-serif;font-weight:800;font-size:29px;line-height:36px;text-align:center}
.services-title{left:34px;top:272px;font-family:'Montserrat',sans-serif;font-weight:800;font-size:20px;letter-spacing:5.5px;color:var(--navy)}
.services-title span{color:var(--red)}
.services-rule{left:34px;top:299px;width:256px;height:1px;background:#555}
.service-list{list-style:none;font-size:13px;line-height:19px;color:var(--navy);font-weight:600}
.service-list li{display:flex;align-items:center;gap:4px}
.service-list svg{width:9px;height:9px;flex:none}
.brand-front{left:444px;top:360px;width:176px;text-align:center;font-family:'Montserrat',sans-serif;font-weight:800;font-size:34px;color:var(--navy)}
.footer-link{top:446px;font-family:'Montserrat',sans-serif;font-weight:500;font-size:15px;color:#fff;display:flex;align-items:center;gap:7px}
.footer-link svg{width:12px;height:12px}

/* back */
.back{left:64px;top:644px;width:683px;height:488px}
.bajo{left:34px;top:22px;font-family:'Oswald',sans-serif;font-weight:600;font-size:21px;line-height:25px;color:#fff}
.ofreciendo{left:34px;top:89px;font-family:'Oswald',sans-serif;font-weight:700;font-size:26px;line-height:34px;color:#fff}
.aceptando{left:34px;top:139px;font-family:'Montserrat',sans-serif;font-weight:700;font-size:25px;line-height:28px;color:#fff}
.locations-tab{left:41px;top:352px;width:231px;height:22px;background:var(--navy);clip-path:polygon(0 0,100% 0,100% 100%,8px 100%);color:#fff;font-size:13px;line-height:22px;padding-left:16px;font-weight:600}
.contact-list{left:40px;top:378px;list-style:none;font-size:13px;line-height:18.7px;color:var(--ink);font-weight:600}
.contact-list li{display:flex;align-items:center;gap:8px}
.contact-list svg{width:10px;height:10px;flex:none}
.brand-back{left:399px;top:58px;width:120px;text-align:center;font-family:'Montserrat',sans-serif;font-weight:800;font-size:22px;color:var(--navy)}
.postage{left:555px;top:37px;width:91px;height:75px;border:1px solid #333;font-family:'Arimo',sans-serif;font-size:10.5px;line-height:13.5px;text-align:center;padding-top:3px;color:var(--ink)}
.address{left:467px;top:272px;width:179px;height:61px;border:1px solid #333;font-family:'Arimo',sans-serif;font-size:9.5px;line-height:11px;color:var(--ink);padding:5px 9px}
.address .route{text-align:center;font-size:8.5px;margin-bottom:12px}
</style>
</head>
<body>
<svg width="0" height="0" style="position:absolute">
  <defs>
    <symbol id="tick" viewBox="0 0 10 10"><circle cx="5" cy="5" r="4.2" fill="none" stroke="#b0000f" stroke-width="1"/><path d="M3 5.1l1.4 1.4L7 3.8" fill="none" stroke="#b0000f" stroke-width="1"/></symbol>
    <symbol id="pin" viewBox="0 0 10 10"><circle cx="5" cy="3.6" r="2.4" fill="none" stroke="#b0000f" stroke-width="1.2"/><path d="M5 6v2.6M2.5 9.2h5" stroke="#b0000f" stroke-width="1.2"/></symbol>
    <symbol id="phone" viewBox="0 0 10 10"><circle cx="5" cy="5" r="4.3" fill="none" stroke="#b0000f" stroke-width="1"/><path d="M3.4 2.8c-.3 1.8.9 3.6 2.9 4.2l.6-.9-1-.6-.5.4c-.7-.4-1.1-1-1.2-1.8l.5-.3-.3-1.1z" fill="#b0000f"/></symbol>
    <symbol id="globe" viewBox="0 0 10 10"><g fill="none" stroke="currentColor" stroke-width=".9"><circle cx="5" cy="5" r="4.2"/><ellipse cx="5" cy="5" rx="1.9" ry="4.2"/><path d="M.8 5h8.4M1.6 2.7h6.8M1.6 7.3h6.8"/></g></symbol>
    <symbol id="mail" viewBox="0 0 12 10"><g fill="none" stroke="currentColor" stroke-width=".9"><rect x=".6" y="1.2" width="10.8" height="7.6"/><path d="M.6 1.2L6 5.6l5.4-4.4M.6 8.8l4-3.7M11.4 8.8l-4-3.7"/></g></symbol>
  </defs>
</svg>

<section class="card front" aria-label="Front">
  <svg class="bg" width="672" height="480" viewBox="0 0 672 480">
    <defs>
      <radialGradient id="teamTone" cx="50%" cy="45%" r="60%">
        <stop offset="0" stop-color="var(--photo-b)"/>
        <stop offset=".55" stop-color="var(--photo-a)"/>
        <stop offset="1" stop-color="#e9edf5"/>
      </radialGradient>
    </defs>
    <rect x="0" y="94" width="337" height="73" fill="var(--red)"/>
    <path d="M375 1 A215 215 0 1 0 640 313" fill="none" stroke="var(--navy)" stroke-width="1.3"/>
    <circle cx="508" cy="166" r="176" fill="url(#teamTone)" stroke="#fff" stroke-width="4" role="img" aria-label="Photo of four smiling doctors and nurses in scrubs and white coats with stethoscopes"/>
    <rect x="0" y="434" width="672" height="46" fill="var(--navy)"/>
    <polygon points="314,434 325,378 336,434" fill="var(--navy)"/>
    <path d="M0 433 L314 433 L325 378 L337 463 L345 433 L672 433" fill="none" stroke="var(--red)" stroke-width="3"/>
  </svg>

  <h1 class="abs headline"><span class="hot">Under new</span> management<br><span class="hot">New</span> staff &amp; <span class="hot">new</span> physicians</h1>
  <p class="abs offering">OFFERING<br>MORE SERVICES</p>
  <p class="abs accepting">ACCEPTING</p>
  <p class="abs new-patients">NEW PATIENTS</p>
  <h2 class="abs services-title">OUR <span>SERVICES:</span></h2>
  <div class="abs services-rule"></div>

  <ul class="abs service-list" style="left:33px;top:308px">
    <li><svg><use href="#tick"/></svg>Primary Care</li>
    <li><svg><use href="#tick"/></svg>Gastroenterology</li>
    <li><svg><use href="#tick"/></svg>Dentistry</li>
    <li><svg><use href="#tick"/></svg>Vascular Surgery</li>
    <li><svg><use href="#tick"/></svg>Psychiatry</li>
    <li><svg><use href="#tick"/></svg>HIV / Infectious Disease</li>
  </ul>
  <ul class="abs service-list" style="left:174px;top:308px">
    <li><svg><use href="#tick"/></svg>Pain Management</li>
    <li><svg><use href="#tick"/></svg>Cardiology</li>
    <li><svg><use href="#tick"/></svg>Dermatology</li>
    <li><svg><use href="#tick"/></svg>Physical Therapy</li>
    <li><svg><use href="#tick"/></svg>Neurology</li>
  </ul>
  <ul class="abs service-list" style="left:313px;top:308px">
    <li><svg><use href="#tick"/></svg>Gynecology</li>
    <li><svg><use href="#tick"/></svg>Podiatry</li>
    <li><svg><use href="#tick"/></svg>Psychology</li>
  </ul>

  <p class="abs brand-front">Orin Care</p>

  <p class="abs footer-link" style="left:36px"><svg><use href="#globe"/></svg>www.orincaregroup.org</p>
  <p class="abs footer-link" style="left:376px"><svg viewBox="0 0 12 10" style="width:14px"><use href="#mail"/></svg>info@orincaregroup.org</p>
</section>

<section class="card back" aria-label="Back" lang="es">
  <svg class="bg" width="683" height="488" viewBox="0 0 683 488">
    <defs>
      <clipPath id="panel"><polygon points="0,0 307,0 395,244 307,488 0,488"/></clipPath>
      <linearGradient id="clinicTone" x1="0" x2="1">
        <stop offset="0" stop-color="#dfe3ea"/>
        <stop offset=".5" stop-color="#c9d6e4"/>
        <stop offset="1" stop-color="#e6e9ee"/>
      </linearGradient>
    </defs>
    <g clip-path="url(#panel)">
      <rect x="0" y="0" width="400" height="86" fill="var(--navy)"/>
      <rect x="0" y="86" width="400" height="40" fill="var(--red)"/>
      <rect x="0" y="126" width="400" height="83" fill="var(--navy)"/>
      <rect x="0" y="209" width="400" height="151" fill="url(#clinicTone)" role="img" aria-label="Photo of a patient and a doctor in face shields and masks talking at a clinic desk"/>
    </g>
    <polygon points="307,0 335,0 420,244 335,488 307,488 395,244" fill="var(--red)"/>
  </svg>

  <p class="abs bajo">Bajo nueva dirección /<br>nuevo personal y nuevos médicos</p>
  <p class="abs ofreciendo">OFRECIENDO MÁS SERVICIOS</p>
  <p class="abs aceptando">ACEPTANDO<br>PACIENTES NUEVOS</p>

  <p class="abs locations-tab" lang="en">Two Locations in the Bronx:</p>
  <ul class="abs contact-list" lang="en">
    <li><svg><use href="#pin"/></svg>North Bronx: 5912 Larkfield Blvd</li>
    <li><svg><use href="#phone"/></svg>718-555-0143</li>
    <li><svg><use href="#pin"/></svg>South Bronx: 614 Dorrin Avenue</li>
    <li><svg><use href="#phone"/></svg>718-555-0187</li>
    <li><svg style="color:var(--red)"><use href="#globe"/></svg>www.orincaregroup.org</li>
  </ul>

  <p class="abs brand-back">Orin Care</p>

  <div class="abs postage" lang="en">PRSRT STD<br>U.S. POSTAGE<br>PAID<br>CITY, STATE<br>PERMIT NO. XXX</div>
  <div class="abs address" lang="en">
    <p class="route">*********ECRWSSQPRL****</p>
    <p>Postal Customer<br>City, State 5-Digit ZIP Code</p>
  </div>
</section>
</body>
</html>
```